PetalDrops - promoting myself as an aromatherapist, VeloMira Wellness Advocate and as Ask Corinna (

This is my first time requesting a web design, so please be patient with me and let me know if you need anything else.
I have a logo which I love and want to use. I've loaded up 3 different file formats, please tell me if you want a different format. I also have web space with web address attached and Wordpress is loaded - www.petaldrops.com.au
I'm frustrated because I don't know how to use WP to the degree I want, but know enough how to add pages, load articles and pictures.
I'm not sure how many pages I need designed. The home page is important. Setting up links is also important. I believe once the overall design is set I can do the rest.
I put 5+ simply because I don't know. Like I said, I know how to add pages. I guess once the overall layout is designed the rest will be easy??
I'd like a home page that has my blog articles with links to the full article. (I've only just begun writing for this)
An information page about veloMIRA and myself (I've begun writing this). A sign up page or link - veloMIRA allocates a personal link for sign up and shopping - mine is www.myvelomira.com/corinna - I have found that people have difficulty finding the 'join and save' button on that page (I find that's a clumsy title), and on my FB page my sign up button goes straight to the sign up page. My FB page is about to change to PetalDrops by Corinna. A link to this on the web site.
A contact me page.
I do articles for essential oils. Plus I also want a Ask Corinna blog. Ask Corinna is similar to Hey Marla. I'm not sure if this should be a separate website or if it can be incorporated into PetalDrops as there IS overlap. I would like to incorporate both.
I have learnt that when people Google veloMIRA in Australia they get US signup pages without realising it. I cannot put veloMIRA Australia on my webpage, but I can put Go Essential Oils Australia or veloMIRA by Corinna in Australia or similar. veloMIRA have strict rules about compliance, but do allow people their own websites.
I want a slick, engaging, user friendly, easily navigated site.
I will update this description as I see ideas come in and understand more of what I want.
I am going to be direct with people as I don't want to waste anyone's time and I don't want anyone to waste mine.
If you don't read this brief don't bother submitting designs.
Please talk to me, I found someone for my logo design who worked with me and as a result we got exactly what I wanted before the due date.
I'm also working on getting a better photo of myself to use. I've also uploaded a couple of documents, unfinished, but enough to get going (I hope!).

Target Market(s)

men, women, mums with bubs/children

Industry/Entity Type

Wellness

Number of Pages Required

5+ page

Requirements
Must have
• Colours are very important and specific - violet.
• Easily navigated.
• Blog and other pages.
Nice to have
• other colours - ice blue, pale yellow, pale pink, royal blue, medium green (think fertilised grass), silver, gold
Should not have
• grey, black

```html
<!DOCTYPE html>
<html lang="en">
<head>
<meta charset="utf-8">
<title>PetalDrops by Corinna</title>
<link rel="stylesheet" href="https://fonts.googleapis.com/css2?family=Dancing+Script:wght@400;600&family=Raleway:wght@400;600;800&family=Open+Sans:wght@400;600&display=swap">
<style>
:root{
  --violet-deep:#5c1a5e;
  --violet:#7a3580;
  --violet-mid:#8f4a94;
  --violet-soft:#a55ca7;
  --lavender:#b99cc6;
  --lilac-bg:#efeef0;
  --band-grey:#e6e5e7;
  --ink:#2b2230;
  --body:#6b6570;
  --white:#ffffff;
  --line:#d9d6db;
}
*{box-sizing:border-box;margin:0;padding:0}
html,body{width:1200px;height:3734px;overflow:hidden;background:var(--white)}
body{font-family:"Open Sans",sans-serif;color:var(--body)}
.page{position:relative;width:1200px;height:3734px;overflow:hidden}
.abs{position:absolute}
.script{font-family:"Dancing Script",cursive;font-weight:400;color:var(--ink)}
.script em{font-style:normal;color:var(--violet)}
.btn{position:absolute;background:var(--violet-deep);color:var(--white);font-family:"Raleway",sans-serif;font-size:19px;display:flex;align-items:center;justify-content:center;border-radius:3px;letter-spacing:.5px}
.section-title{position:absolute;left:0;width:1200px;text-align:center;font-size:48px}

/* hero */
.hero{position:absolute;left:0;top:0;width:1200px;height:715px;overflow:hidden}
.hero-photo{position:absolute;inset:0;background:linear-gradient(100deg,#f4f1f3 0%,#e9e2e6 35%,#d7cbd0 60%,#cdbfc2 80%,#e6dfdc 100%)}
.hero-oils{position:absolute;left:620px;top:280px;width:520px;height:310px;border-radius:50% 50% 0 0;background:radial-gradient(ellipse at 60% 50%,#9b6a3a 0%,#7d8b5a 45%,rgba(200,190,185,0) 75%)}
.nav{position:absolute;top:50px;left:0;width:1200px;height:42px;font-family:"Raleway",sans-serif;font-size:19px;color:var(--ink)}
.nav a{position:absolute;top:0;height:42px;line-height:42px;color:var(--ink);text-decoration:none}
.nav a.active{background:var(--violet-deep);color:var(--white);padding:0 12px;border-radius:2px}
.brand{position:absolute;left:448px;top:16px;width:274px;text-align:center;font-family:"Raleway",sans-serif;font-weight:600;font-size:40px;color:var(--violet-mid)}
.brand small{display:block;font-size:13px;font-weight:600;color:var(--violet-mid);margin-top:-4px}
.hero h1{position:absolute;left:80px;top:228px;font-family:"Raleway",sans-serif;font-weight:800;font-size:37px;line-height:50px;color:var(--violet-deep);text-transform:uppercase}
.hero p{position:absolute;left:80px;top:410px;width:380px;font-size:15px;line-height:24px;color:var(--ink)}
.hero-curve{position:absolute;left:0;top:0}

/* welcome */
.welcome-text{position:absolute;left:80px;top:832px;width:600px;font-size:15px;line-height:24px}
.welcome-text p+p{margin-top:20px}
.video{position:absolute;left:725px;top:834px;width:398px;height:194px;background:linear-gradient(110deg,#7a6a60 0%,#a89a90 45%,#d8cdc7 100%);border:2px solid #8b7f86}
.play{position:absolute;left:180px;top:80px;width:38px;height:28px;background:var(--white);border-radius:6px}
.play:after{content:"";position:absolute;left:14px;top:8px;border-left:12px solid var(--ink);border-top:6px solid transparent;border-bottom:6px solid transparent}

/* brand band */
.band{position:absolute;left:0;top:1113px;width:1200px;height:414px;background:linear-gradient(90deg,#c7b4d2 0%,#a98ab9 30%,#8a4f92 55%,#7a3580 80%,#6d2c72 100%)}
.band-photo{position:absolute;left:0;top:0;width:760px;height:414px;background:radial-gradient(ellipse at 25% 45%,#3a2a2a 0%,#5c4a5c 18%,#a585c0 45%,rgba(138,79,146,0) 80%)}
.portrait{position:absolute;left:483px;top:119px;width:224px;height:230px;background:var(--white);padding:8px}
.portrait div{width:100%;height:100%;background:linear-gradient(180deg,#d9d6d8 0%,#b6b0b4 60%,#3b3d48 100%)}
.band-name{position:absolute;left:745px;top:48px;font-family:"Raleway",sans-serif;font-weight:400;font-size:40px;line-height:52px;color:var(--white)}
.band p{position:absolute;left:745px;top:117px;width:370px;font-size:15px;line-height:24px;color:var(--white)}
.band .btn{left:745px;top:277px;width:156px;height:50px;background:var(--violet-deep)}

/* products */
.products{position:absolute;left:80px;top:1668px;width:1040px;height:237px;display:flex}
.product{flex:1;position:relative;border-right:1px solid var(--line)}
.product:last-child{border-right:none}
.product .shot{position:absolute;left:12px;top:20px;right:12px;height:155px;background:radial-gradient(ellipse at 40% 50%,#a07ec2 0%,#d6c8de 45%,#ffffff 80%)}
.product:nth-child(2n) .shot{background:radial-gradient(ellipse at 60% 50%,#c46a2a 0%,#b79ac9 35%,#f5f2f6 75%)}
.product span{position:absolute;left:0;width:100%;top:195px;text-align:center;font-size:19px;color:var(--ink)}
.rule{position:absolute;left:80px;top:1935px;width:1040px;height:1px;background:var(--line)}

/* features */
.features{position:absolute;left:0;top:2062px;width:1200px;height:271px;background:var(--band-grey)}
.feature{position:absolute;top:0;width:316px;height:271px;text-align:center}
.feature svg{position:absolute;left:118px;top:60px}
.feature b{position:absolute;left:0;width:100%;top:166px;font-family:"Dancing Script",cursive;font-weight:400;font-size:28px;color:var(--ink)}
.feature i{position:absolute;left:0;top:212px;width:100%;height:4px;background:var(--violet-deep)}

/* testimonial */
.testimonial{position:absolute;left:0;top:2333px;width:1200px;height:262px;background:linear-gradient(90deg,#6e2b74 0%,#7d3a84 55%,#9a6ea6 80%,#8a5a96 100%)}
.testimonial h2{position:absolute;left:80px;top:62px;font-size:48px;line-height:58px;color:var(--white)}
.testimonial .divider{position:absolute;left:346px;top:28px;width:1px;height:206px;background:rgba(255,255,255,.5)}
.avatar{position:absolute;left:431px;top:75px;width:104px;height:102px;background:linear-gradient(180deg,#ece8ea 0%,#b8b2b6 60%,#3b3d48 100%)}
.quote{position:absolute;left:568px;top:74px;width:520px;font-size:15px;line-height:29px;color:var(--white)}
.dots{position:absolute;left:1045px;top:215px;display:flex;gap:4px}
.dots span{width:15px;height:15px;border-radius:50%;border:2px solid var(--white)}
.dots span.on{background:var(--white)}

/* contact */
.contact-intro{position:absolute;left:270px;top:2704px;width:660px;text-align:center;font-size:15px;line-height:26px}
.field{position:absolute;left:281px;width:314px;height:42px;border:1px solid var(--line);border-radius:4px;font-size:14px;padding:11px 12px;color:#8d8791;background:var(--white)}
.message{position:absolute;left:605px;top:2801px;width:311px;height:145px;border:1px solid var(--line);border-radius:14px;font-size:14px;padding:11px 20px;color:#8d8791}

/* blogs */
.blogs{position:absolute;left:0;top:3063px;width:1200px;height:500px;background:var(--lilac-bg)}
.post{position:absolute;top:124px;width:530px;height:160px}
.post .thumb{position:absolute;left:0;top:0;width:251px;height:157px}
.post .date{position:absolute;left:0;top:0;width:52px;height:66px;background:#1f1a22;color:var(--white);text-align:center;font-size:24px;line-height:32px;padding-top:4px}
.post .date small{display:block;font-size:13px;line-height:16px}
.post h3{position:absolute;top:6px;font-weight:400;font-size:20px;white-space:nowrap;color:var(--violet-deep)}
.post .sep{position:absolute;height:1px;background:var(--line)}
.post p{position:absolute;top:58px;width:245px;font-size:15px;line-height:24px}
.post a{position:absolute;top:140px;font-family:"Dancing Script",cursive;font-size:17px;color:var(--ink);text-decoration:underline}

/* footer */
.footer{position:absolute;left:0;top:3410px;width:1200px;height:324px}
.footer-links{position:absolute;left:80px;top:145px;font-size:15px;color:var(--white);display:flex;gap:33px}
.social{position:absolute;left:940px;top:140px;display:flex;gap:30px}
.social span{width:18px;height:18px;border-radius:50%;background:var(--white);opacity:.9}
.footer-rule{position:absolute;left:80px;width:1040px;height:1px;background:rgba(255,255,255,.45)}
.info{position:absolute;top:214px;display:flex;align-items:center;gap:14px;font-size:14px;line-height:20px;color:var(--white)}
.info svg{flex:none}
.copyright{position:absolute;left:0;top:285px;width:1200px;text-align:center;font-size:14px;color:var(--white)}
.footer-mark{position:absolute;left:0;width:1200px;top:44px;text-align:center;font-family:"Raleway",sans-serif;font-weight:600;font-size:22px;color:var(--white)}
</style>
</head>
<body>
<div class="page">

  <header class="hero">
    <div class="hero-photo" role="img" aria-label="Woman relaxing during a massage with amber oil bottles and rosemary"></div>
    <div class="hero-oils" role="img" aria-label="Amber essential oil bottles, rosemary sprigs and stones"></div>
    <svg class="hero-curve" width="1200" height="715" viewBox="0 0 1200 715">
      <path d="M0 505 Q560 860 1200 545 L1200 715 L0 715 Z" fill="var(--lilac-bg)"/>
      <path d="M0 505 Q560 860 1200 545" fill="none" stroke="var(--violet-soft)" stroke-width="5"/>
    </svg>
    <nav class="nav">
      <a class="active" style="left:75px">HOME</a>
      <a style="left:180px">ABOUT</a>
      <a style="left:279px">PETALDROPS</a>
      <a style="left:755px">HEALTHY LIVING</a>
      <a style="left:936px">BLOG</a>
      <a style="left:1021px">CONTACT</a>
    </nav>
    <div class="brand">PetalDrops<small>by Corinna</small></div>
    <h1>Revolutionizing the way<br>families manage their<br>health</h1>
    <p>We harness nature's most powerful elements and share these gifts through our global community of Wellness Advocates.</p>
  </header>

  <section class="welcome">
    <h2 class="section-title script" style="top:738px">Welcome To <em>PetalDrops</em></h2>
    <div class="welcome-text">
      <p>Lorem Ipsum is simply dummy text of the printing and typesetting industry. Lorem Ipsum has been the industry's standard dummy text ever since the 1500s, when an unknown printer took a galley of type and scrambled it to make a type specimen book.</p>
      <p>Lorem Ipsum is simply dummy text of the printing and typesetting industry. Lorem Ipsum has been the industry's standard dummy text ever since the 1500.</p>
    </div>
    <div class="btn" style="left:77px;top:1008px;width:157px;height:48px">READ MORE</div>
    <div class="video" role="img" aria-label="Video still of a massage treatment"><span class="play"></span></div>
  </section>

  <section class="band">
    <div class="band-photo" role="img" aria-label="Essential oil bottle among lavender sprigs"></div>
    <div class="portrait"><div role="img" aria-label="Portrait of Corinna"></div></div>
    <h2 class="band-name">VeloMira</h2>
    <p>Lorem Ipsum is simply dummy text of the printing and typesetting industry. Lorem Ipsum has been the industry's standard dummy text ever since the 1500s, when an unknown printer took a galley of type and scrambled it to make a type specimen book.</p>
    <div class="btn">CONTACT ME</div>
  </section>

  <section class="product-list">
    <h2 class="section-title script" style="top:1560px">Essential Oils <em>Products</em></h2>
    <div class="products">
      <div class="product"><div class="shot" role="img" aria-label="Lavender with an oil jar"></div><span>Product Name</span></div>
      <div class="product"><div class="shot" role="img" aria-label="Oil bottle with lavender and towel"></div><span>Product Name</span></div>
      <div class="product"><div class="shot" role="img" aria-label="Lavender with an oil jar"></div><span>Product Name</span></div>
      <div class="product"><div class="shot" role="img" aria-label="Oil bottle with lavender and towel"></div><span>Product Name</span></div>
    </div>
    <div class="rule"></div>
    <div class="btn" style="left:510px;top:1960px;width:178px;height:50px">View More</div>
  </section>

  <section class="features">
    <div class="feature" style="left:74px">
      <svg width="80" height="90" viewBox="0 0 80 90"><path d="M8 40h16v44H8z M28 42 L44 12 Q50 4 54 12 L50 36 H70 Q78 38 76 46 L70 78 Q68 84 60 84 H28 Z" fill="var(--violet-deep)"/></svg>
      <b>Healthy Living</b><i></i>
    </div>
    <div class="feature" style="left:442px">
      <svg width="80" height="90" viewBox="0 0 80 90"><circle cx="40" cy="12" r="10" fill="var(--violet-deep)"/><path d="M12 20 L32 36 V52 L20 86 H32 L40 62 L48 86 H60 L48 52 V36 L68 20 L62 14 L40 30 L18 14 Z" fill="var(--violet-deep)"/></svg>
      <b>Do It Yourself</b><i></i>
    </div>
    <div class="feature" style="left:809px">
      <svg width="80" height="90" viewBox="0 0 80 90"><circle cx="40" cy="48" r="34" fill="none" stroke="var(--violet-deep)" stroke-width="7"/><circle cx="40" cy="48" r="20" fill="none" stroke="var(--violet-deep)" stroke-width="7"/><circle cx="40" cy="48" r="7" fill="var(--violet-deep)"/><path d="M40 48 L70 18" stroke="var(--violet-deep)" stroke-width="4"/></svg>
      <b>Ready For Anything</b><i></i>
    </div>
  </section>

  <section class="testimonial">
    <h2 class="script">What Our<br>Client Say</h2>
    <div class="divider"></div>
    <div class="avatar" role="img" aria-label="Client portrait"></div>
    <p class="quote">Lorem Ipsum is simply dummy text of the printing and typesetting industry. Lorem Ipsum has been the industry's standard dummy text ever.<br>-MAYA TOLLEN</p>
    <div class="dots"><span></span><span class="on"></span><span></span><span></span></div>
  </section>

  <section class="contact">
    <h2 class="section-title script" style="top:2616px">Get in <em>Touch With Us</em></h2>
    <p class="contact-intro">Lorem Ipsum is simply dummy text of the printing and typesetting industry. Lorem Ipsum has been the industry's standard dummy text ever.</p>
    <div class="field" style="top:2801px">Name</div>
    <div class="field" style="top:2852px">Email Id</div>
    <div class="field" style="top:2903px">Contact No.</div>
    <div class="message">Message here</div>
    <div class="btn" style="left:520px;top:2958px;width:157px;height:52px">SUBMIT</div>
  </section>

  <section class="blogs">
    <h2 class="section-title script" style="top:22px">Our <em>Blogs</em></h2>
    <article class="post" style="left:80px">
      <div class="thumb" role="img" aria-label="Oil bottles with white flowers on green leaves" style="background:linear-gradient(120deg,#4e7a2a,#a7c061 55%,#e8e2c8)"></div>
      <div class="date">20<small>Nov.</small></div>
      <h3 style="left:264px">Lorem Ipsum is simply.</h3>
      <div class="sep" style="left:264px;top:44px;width:245px"></div>
      <p style="left:264px">Lorem Ipsum is simply dummy text of the printing and typesetting industry.</p>
      <div class="sep" style="left:264px;top:134px;width:245px"></div>
      <a style="left:264px">READ MORE</a>
    </article>
    <article class="post" style="left:590px">
      <div class="thumb" role="img" aria-label="Glass oil bottles with dried orange slices and salt" style="width:256px;background:linear-gradient(120deg,#c86a2e,#e9b27a 50%,#f1e6dc)"></div>
      <div class="date">19<small>Nov.</small></div>
      <h3 style="left:276px">Lorem Ipsum simply text.</h3>
      <div class="sep" style="left:276px;top:44px;width:245px"></div>
      <p style="left:276px">Lorem Ipsum is simply dummy text of the printing and typesetting industry.</p>
      <div class="sep" style="left:276px;top:134px;width:245px"></div>
      <a style="left:276px">READ MORE</a>
    </article>
  </section>

  <footer class="footer">
    <svg class="abs" style="left:0;top:0" width="1200" height="324" viewBox="0 0 1200 324">
      <path d="M0 80 Q600 -60 1200 80 L1200 324 L0 324 Z" fill="var(--violet-soft)"/>
      <path d="M0 80 Q600 -60 1200 80" fill="none" stroke="var(--violet-deep)" stroke-width="4"/>
    </svg>
    <div class="footer-mark">PetalDrops</div>
    <div class="footer-links"><span>Home</span><span>About</span><span>PetalDrops</span><span>Healthy Living</span><span>Blog</span><span>Contact Us</span></div>
    <div class="social"><span></span><span></span><span></span></div>
    <div class="footer-rule" style="top:180px"></div>
    <div class="info" style="left:80px">
      <svg width="34" height="34" viewBox="0 0 34 34"><circle cx="17" cy="17" r="15" fill="none" stroke="#fff" stroke-width="2"/><path d="M17 8a6 6 0 0 1 6 6c0 5-6 11-6 11s-6-6-6-11a6 6 0 0 1 6-6z" fill="#fff"/><circle cx="17" cy="14" r="2" fill="var(--violet-soft)"/></svg>
      <span>123,Lorem Ipsum dummy<br>Country ZIP Code</span>
    </div>
    <div class="info" style="left:370px">
      <svg width="34" height="34" viewBox="0 0 34 34"><circle cx="17" cy="17" r="16" fill="#fff"/><rect x="12" y="8" width="10" height="18" rx="2" fill="var(--violet-deep)"/><rect x="14" y="11" width="6" height="10" fill="#fff"/></svg>
      <span>+61 400 555 010</span>
    </div>
    <div class="info" style="left:645px">
      <svg width="34" height="34" viewBox="0 0 34 34"><circle cx="17" cy="17" r="16" fill="#fff"/><path d="M9 14 Q17 6 25 14 L24 18 H21 V15 H13 V18 H10 Z M12 19 H22 V26 H12 Z" fill="var(--violet-deep)"/></svg>
      <span>+61 400 555 010</span>
    </div>
    <div class="info" style="left:900px">
      <svg width="34" height="34" viewBox="0 0 34 34"><circle cx="17" cy="17" r="16" fill="#fff"/><rect x="9" y="11" width="16" height="12" fill="none" stroke="var(--violet-deep)" stroke-width="2"/><path d="M9 11 L17 18 L25 11" fill="none" stroke="var(--violet-deep)" stroke-width="2"/></svg>
      <span>hello@petaldrops.com.au</span>
    </div>
    <div class="footer-rule" style="top:266px"></div>
    <p class="copyright">© <b>PetalDrops by Corinna</b> - 2016 All Rights Reserved</p>
  </footer>

</div>
</body>
</html>
```